A4 Tri-fold Brochure for Sedation Dentist Specialist Dr. Marlon and Sedation Dentistry.

I would like to create an A4 tri-fold brochure for our Dental Sedation Specialist Dr. Marlon Vesk. Please carefully select the most suitable highlights from his bio below.

This brochure has two parts. Highlighting what makes Dr. Marlon Vesk unique and trustworthy. Include a picture of him (attached). The second part is about sedation dentistry. All you need to know here: http://www.calmchairplex.com/how-does-sedation-dentistry-work

Avoid making it too wordy.

Meet Dr. Roh Dak Marlon Vesk, DDS

Inspired to Become a Dentist:
As a child, Dr. Marlon Vesk always felt stressed whenever he had to see a dentist. He knew that he wanted to become a dentist to help put patients completely at ease while they experienced quality dental care.

He is passionate about giving patients the healthy, beautiful smiles they deserve. “I find it fulfilling when I can see my patients’ beautiful smiles and how they can finally appreciate the joy of eating with a healthy set of teeth. However, what I love most about my job is the ability to provide a stress-free and comfortable experience at the dentist’s office, particularly for children, through sedation and general anesthesia.”

Educational Achievements:
Before becoming a dentist, Dr. Marlon Vesk earned his undergraduate degree at the Pellridge University of Northern Basin where he received a Bachelor of Medical Science Honor Specialization degree with distinction in biochemistry. He then completed his Doctor of Dental Surgery degree with honors at the Harwick Crest University. While there, he received the Elmer Drayce Medal in his class for outstanding achievement in anesthesia. He then pursued his three-year residency as well as a master’s degree in dental anesthesia at the Harwick Crest University.

So he can provide his patients with the latest in dentistry, Dr. Marlon Vesk enjoys pursuing additional knowledge, particularly in the areas of dental anesthesia as well as advanced technologies in dentistry. He is currently part of the Molar Horizon Circle study club and has enrolled in the Core Rootwork Mini- Residency Program. He also serves as a clinical instructor at the Plenvo Center at the Harwick Crest University.

Association Memberships:
In addition to his academic credentials, Dr. Marlon Vesk is a member of several associations:
The Vantley Board of Dental Surgeons of Quarrow (VBDSQ)
Dental Norvane Guild of Dental Anesthesia (NGDA)
Brisken Forum of Dental Anesthesia (BFDA)
Quarrow Dental Federation (QDF)
Outside the Practice

When he’s not at the practice, Dr. Marlon Vesk enjoys spending time with his wife Wren and their two poodles Pippa and Biscuit, who are spoiled rotten! “Wren and I love taking our dogs out on hikes and to the dog park on weekends. I also enjoy a wide range of activities from model building and playing the piano to soccer, gym and archery.” He stays fit by working out at the local Fitwell gym, and he likes to walk in Ashbury Lake Park and Dunmore Field Park.

Dr. Marlon Vesk considers himself to be a kid at heart. He is a big fan of superheroes and animated movies. “I get really excited about any upcoming superhero or Zentry Lumo movies. Till this day, I still collect superhero toy figures.”

He supports the BrightCot Foundation as well as the Quarrow League for the Protection of Animal Welfare (LPAW).

Experience outstanding dental care with our highly skilled dentist. Contact us today to schedule an appointment with Dr. Marlon Vesk! He speaks English, Cantonese, and Mandarin.

Target Market(s)

Mothers with young kids.

Industry/Entity Type

Dental

Font styles to use
Sans Serif

Requirements
Should not have
• Prices

```html
<!DOCTYPE html>
<html lang="en">
<head>
<meta charset="utf-8">
<title>Meet Dr. Marlon Vesk – Brochure Outside Spread</title>
<link rel="stylesheet" href="https://fonts.googleapis.com/css2?family=Questrial&family=Montserrat:ital,wght@0,700;1,600;1,700&display=swap">
<style>
  :root {
    --cyan: #00ffff;
    --cyan-deep: #17e6ef;
    --orange: #ff8000;
    --white: #ffffff;
    --ink: #4a4a4a;
    --shadow: #6b6b6b;
    --photo-dark: #2a2f4a;
    --photo-warm: #8a7366;
  }
  * { margin: 0; padding: 0; box-sizing: border-box; }
  html, body { width: 1200px; height: 846px; overflow: hidden; background: var(--white); }
  .spread { position: relative; width: 1200px; height: 846px; display: flex; }

  .panel { position: relative; height: 846px; }
  .panel--story { width: 390px; background: var(--white); }
  .panel--contact { width: 406px; background: var(--cyan); }
  .panel--cover { width: 404px; background: var(--cyan); overflow: hidden; }

  .story__title {
    position: absolute; left: 15px; top: 62px;
    font-family: "Montserrat", sans-serif; font-weight: 700; font-style: italic;
    font-size: 32px; color: var(--cyan-deep); letter-spacing: 0.2px;
  }
  .story__body {
    position: absolute; left: 15px; top: 108px; width: 350px;
    font-family: "Questrial", sans-serif; font-size: 19px; line-height: 34.6px;
    color: var(--ink);
  }
  .story__quote {
    position: absolute; left: 11px; top: 698px; width: 355px; height: 140px;
    background: var(--cyan); border-radius: 10px;
    box-shadow: 3px 3px 0 var(--shadow);
    padding: 2px 12px 0 4px;
    font-family: "Questrial", sans-serif; font-style: italic; font-size: 19px;
    line-height: 34.6px; color: var(--white);
  }

  .contact__causes {
    position: absolute; left: 30px; top: 20px; width: 350px;
    font-family: "Questrial", sans-serif; font-size: 19px; line-height: 34.6px;
    color: var(--white);
  }
  .contact__tagline {
    position: absolute; left: 0; top: 228px; width: 406px; text-align: center;
    font-family: "Montserrat", sans-serif; font-weight: 600; font-style: italic;
    font-size: 18.5px; line-height: 34.6px; color: var(--white);
  }
  .contact__cta {
    position: absolute; left: 0; top: 332px; width: 406px; text-align: center;
    font-family: "Questrial", sans-serif; font-size: 19px; line-height: 34.6px;
    color: var(--white);
  }

  .cover__band { position: absolute; left: 0; top: 0; width: 404px; height: 142px; background: var(--orange); }
  .cover__meet {
    position: absolute; left: 0; top: 42px; width: 390px; text-align: center;
    font-family: "Montserrat", sans-serif; font-weight: 700;
    font-size: 60px; line-height: 1; color: var(--cyan);
  }
  .cover__art { position: absolute; left: 0; top: 0; }
  .cover__frame {
    position: absolute; left: 14px; top: 30px; width: 376px; height: 798px;
    border: 1.5px solid var(--white);
  }
  .cover__name {
    position: absolute; left: 0; top: 733px; width: 404px; text-align: center;
    font-family: "Montserrat", sans-serif; font-weight: 700;
    font-size: 21px; color: var(--white);
  }
</style>
</head>
<body>
<main class="spread">
  <section class="panel panel--story">
    <h2 class="story__title">Outside the Practice</h2>
    <p class="story__body">When he’s not at the practice, Dr. Marlon Vesk enjoys spending time with his wife Wren and their two poodles Pippa and Biscuit, who are spoiled rotten! “Wren and I love taking our dogs out on hikes and to the dog park on weekends. I also enjoy a wide range of activities from model building and playing the piano to soccer, gym and archery.” He stays fit by working out at the local Fitwell gym, and he likes to walk in Ashbury Lake Park and Dunmore Field Park. Dr. Marlon Vesk considers himself to be a kid at heart. He is a big fan of superheroes and animated movies.</p>
    <blockquote class="story__quote">“I get really excited about any up-coming superhero or Zentry Lumo movies. Till this day, I still collect superhero toy figures.”</blockquote>
  </section>

  <section class="panel panel--contact">
    <p class="contact__causes">He supports the BrightCot Foundation as well as the Quarrow League for the Protection of Animal Welfare (LPAW).</p>
    <p class="contact__tagline">Experience outstanding Dental<br>Care with our highly skilled dentist.</p>
    <p class="contact__cta">Contact us today to schedule an<br>appointment with<br>Dr. Marlon Vesk! He speaks;<br>English, Cantonese, and Mandarin.</p>
  </section>

  <section class="panel panel--cover">
    <div class="cover__band"></div>
    <svg class="cover__art" width="404" height="846" viewBox="0 0 404 846">
      <defs>
        <linearGradient id="portraitTone" x1="0" y1="0" x2="0" y2="1">
          <stop offset="0" stop-color="var(--photo-warm)"/>
          <stop offset="0.45" stop-color="#5a4f5c"/>
          <stop offset="1" stop-color="var(--photo-dark)"/>
        </linearGradient>
      </defs>
      <path d="M0,430 C40,560 200,690 404,706 L404,690 C210,676 50,560 0,420 Z" fill="var(--orange)"/>
      <path role="img" aria-label="Portrait photo of Dr. Marlon Vesk in navy scrubs with a stethoscope, in the clinic"
            d="M4,146 H404 V688 C210,674 52,560 4,424 Z" fill="url(#portraitTone)"/>
    </svg>
    <div class="cover__meet">Meet</div>
    <div class="cover__frame"></div>
    <p class="cover__name">Dr. Roh Dak Marlon Vesk,DDS</p>
  </section>
</main>
</body>
</html>
```